Music Studio and Store Business Card and Logo Design

We need a business card and logo design for an existing Music Studio (Piano and Voice) which will soon expand to offer retail sheet music for all instruments including voice. The expanding store will not sell or lease instruments. We are a well known Fine Arts Studio for instruction to children, college students, and adults with 42 enrolled students and a wait list. We want something with simple elegance, but not archaic. Even a sleek modern look is okay. We do not want something childish or too fun looking because we do serve ages 5 - 62. We would also like the logo workable/transferable to signage for our new location opening in March. We like classic burgundy, black, deep blues, but are open to other suggestions. We included our studio brochure so you can get to know us a little better and some images we thought were interesting with the use of clef signs for the & and using note heads for the bottom or top of the letter "H"

Target Market(s)

All ages

Industry/Entity Type

Business

Contact Information for Business Card

H&H Music StudioPlattsburgh, NYWanda J. Haby and Osric M. Dunleavy, Owners

Requirements
Must have
• Phone Number: (480) 615-7094
• Website: www.rtcadenzaroom.example
Nice to have
• Email: lorna@rtcadenzaroom.example
Should not have
• Any instruments on the card other than piano. Instrument pix is not a necessity.

```html
<!DOCTYPE html>
<html lang="en">
<head>
<meta charset="utf-8">
<title>R&amp;T Music Studio – Business Card</title>
<link rel="stylesheet" href="https://fonts.googleapis.com/css2?family=Open+Sans:wght@400;600&display=swap">
<style>
  :root {
    --stage: #000000;
    --card-white: #ffffff;
    --brand-red: #ff0a0a;
    --brand-red-deep: #d40808;
    --ink: #111111;
  }
  * { margin: 0; padding: 0; box-sizing: border-box; }
  html, body {
    width: 1200px;
    height: 900px;
    overflow: hidden;
    background: var(--stage);
    font-family: "Open Sans", Arial, sans-serif;
  }
  .stage { position: relative; width: 1200px; height: 900px; }

  .card { position: absolute; top: 275px; width: 477px; height: 293px; }

  .card-front {
    left: 116px;
    background: var(--card-white);
    border-radius: 0 56px 0 56px;
  }
  .card-back {
    left: 622px;
    top: 276px;
    height: 292px;
    background: var(--brand-red);
    border-radius: 56px 0 56px 0;
  }

  .brand-lockup {
    position: absolute;
    display: flex;
    align-items: center;
    gap: 10px;
    white-space: nowrap;
  }
  .brand-mark {
    width: 14px; height: 14px;
    border-radius: 50%;
    background: var(--brand-red);
    flex: none;
  }
  .brand-name {
    font-weight: 600;
    letter-spacing: 0.04em;
    text-transform: uppercase;
    color: var(--brand-red);
  }
  .card-front .brand-lockup { left: 120px; top: 96px; }
  .card-front .brand-name { font-size: 21px; }

  .card-back .brand-lockup { left: 84px; top: 146px; transform: translateY(-50%); }
  .card-back .brand-mark { width: 18px; height: 18px; background: var(--brand-red-deep); }
  .card-back .brand-name { font-size: 26px; color: var(--brand-red-deep); }

  .owners { position: absolute; left: 26px; top: 192px; }
  .owner-name {
    font-size: 16px;
    font-weight: 600;
    color: var(--brand-red);
    line-height: 23px;
  }
  .owner-role { font-size: 14px; color: var(--ink); line-height: 19px; }

  .contact { position: absolute; right: 27px; top: 170px; text-align: right; white-space: nowrap; }
  .contact-label { font-size: 14px; font-weight: 600; color: var(--brand-red); line-height: 20px; }
  .contact-line { font-size: 13px; color: var(--ink); line-height: 20px; }
</style>
</head>
<body>
  <main class="stage">
    <section class="card card-front">
      <div class="brand-lockup">
        <span class="brand-mark"></span>
        <span class="brand-name">R&amp;T Music Studio</span>
      </div>
      <div class="owners">
        <p class="owner-name">Lorna K. Petrov</p>
        <p class="owner-name">Osric M. Dunleavy</p>
        <p class="owner-role">Owners</p>
      </div>
      <div class="contact">
        <p class="contact-label">Address</p>
        <p class="contact-line">Alder Falls, NY</p>
        <p class="contact-line">(480) 615-7094</p>
        <p class="contact-line">www.rtcadenzaroom.example</p>
      </div>
    </section>

    <section class="card card-back">
      <div class="brand-lockup">
        <span class="brand-mark"></span>
        <span class="brand-name">R&amp;T Music Studio</span>
      </div>
    </section>
  </main>
</body>
</html>
```